TRENDY & MODERN BUSINESS CARD DESIGN for Media Company *

I need a minimalistic - clean - modern and professional business card layout and design for MEDIA & PHOTOGRAPHY STUDIO.

We do NOT have a logo, and not really looking for one - but rather excellent typography and design. We would consider the 3 as a focal point.

We do personal and commercial photography.

Target Market(s)

Personal and commercial photography clientele

Contact Information for Business Card

ZUB size - from zub.com / size guidelines are enclosed in the brief

Font styles to use
Sans Serif

Colors
f78f20
eda3c7
cee9f5
0555a3
e667a6
fbf289

Requirements
Must have
• Clean lines - Modern layout
Nice to have
• All blue background as an option - use color palette in brief please.
Should not have
• Old fashion fonts and regular fonts.

```html
<!DOCTYPE html>
<html lang="en">
<head>
<meta charset="utf-8">
<title>Halcyon Frame – Business Card</title>
<link rel="stylesheet" href="https://fonts.googleapis.com/css2?family=Lato:wght@300;400;700;900&display=swap">
<style>
  :root {
    --stage: #3b3b3b;
    --sky: #cee9f5;
    --sky-deep: #bddcee;
    --brand-blue: #0a55a3;
    --ink-dark: #10304f;
    --butter: #fbf289;
    --white: #ffffff;
  }
  * { box-sizing: border-box; margin: 0; padding: 0; }
  html, body {
    width: 1200px; height: 755px; overflow: hidden;
    background: var(--stage);
    font-family: "Lato", Helvetica, Arial, sans-serif;
  }
  .card {
    position: absolute;
    top: 216px;
    width: 500px; height: 290px;
    overflow: hidden;
  }
  /* Front */
  .card-front { left: 84px; background: var(--sky); }
  .decor-area {
    position: absolute; left: 0; top: 0; width: 300px; height: 210px;
    background: radial-gradient(ellipse at 45% 40%, var(--sky-deep) 0%, var(--sky) 70%);
  }
  .brand {
    position: absolute; left: 23px; top: 226px;
    color: var(--brand-blue);
    font-size: 23px; font-weight: 700; line-height: 1;
  }
  .tagline {
    position: absolute; left: 23px; top: 256px;
    color: var(--ink-dark);
    font-size: 9.5px; font-weight: 700; letter-spacing: 1.6px;
  }
  .contact-panel {
    position: absolute; left: 265px; top: 161px; width: 235px; height: 129px;
    background: var(--brand-blue);
    color: var(--white);
    padding: 26px 0 0 24px;
  }
  .contact-row {
    display: flex; align-items: flex-start;
    font-size: 13px; line-height: 16px; margin-bottom: 11px;
  }
  .contact-row svg { width: 11px; height: 11px; margin: 2px 8px 0 0; flex: none; fill: var(--white); }
  /* Back */
  .card-back { left: 618px; background: var(--brand-blue); color: var(--white); text-align: center; }
  .holder-name {
    position: absolute; left: 0; right: 0; top: 136px;
    font-size: 25px; font-weight: 300; letter-spacing: 0.3px; line-height: 1;
  }
  .holder-name strong { font-weight: 700; }
  .holder-role {
    position: absolute; left: 0; right: 0; top: 170px;
    color: var(--butter);
    font-size: 11px; font-weight: 700; letter-spacing: 2.6px;
  }
  .city-list {
    position: absolute; left: 0; right: 0; top: 257px;
    font-size: 11.5px; font-weight: 700; letter-spacing: 2px;
  }
  .city-list .dot { margin: 0 10px; }
</style>
</head>
<body>
  <section class="card card-front">
    <div class="decor-area" role="img" aria-label="Large faint script letter decoration"></div>
    <h1 class="brand">HALCYON FRAME</h1>
    <p class="tagline">SEEING LIGHT.&nbsp; SHAPING STORIES.</p>
    <div class="contact-panel">
      <div class="contact-row">
        <svg viewBox="0 0 12 12" aria-hidden="true"><path d="M1 3.5C1 2 3 1.5 6 1.5S11 2 11 3.5V5H8.5V3.8H3.5V5H1z M2.5 6h7L11 10.5H1z"/></svg>
        <span>(305) 555-0142</span>
      </div>
      <div class="contact-row">
        <svg viewBox="0 0 12 12" aria-hidden="true"><path d="M1 2.5h10v7H1z" fill="none" stroke="#fff" stroke-width="1.2"/><path d="M1 2.5l5 4 5-4" fill="none" stroke="#fff" stroke-width="1.2"/></svg>
        <span>mari@halcyonframe.com</span>
      </div>
      <div class="contact-row">
        <svg viewBox="0 0 12 12" aria-hidden="true"><path d="M6 1L0.5 6h1.8v5h3V8h1.4v3h3V6h1.8z"/></svg>
        <span>2200 Harbor Avenue,<br>9th Floor, Miami, FL 33130</span>
      </div>
    </div>
  </section>

  <section class="card card-back">
    <h2 class="holder-name">MARIELA <strong>SANTOS</strong></h2>
    <p class="holder-role">FOUNDER &amp; MEDIA DIRECTOR</p>
    <p class="city-list">MIAMI<span class="dot">·</span>AUSTIN<span class="dot">·</span>DENVER<span class="dot">·</span>TULUM<span class="dot">·</span>LISBOA</p>
  </section>
</body>
</html>
```